intraoral tooth cleaning device requires JAZZY NEW PACKAGING

I already have a logo design for my product "GUMBRA" but I need a sharply designed packaging. Something that is bright and stands out.
Gumbra is an anatomically and ergonomically correct dental plaque remover. It
"Makes Every Smile Brightly Fresh".
Go to my website gumbrapick.example to get the logo design and the look and feel of the product. Also there is more information about the product.
I am trying to get a package with 10 pieces of Gumbra in each package. I also would be interested in packaging for 20 pieces also..I would like the package to be like a pack of cigarettes and fit in a shirt pocket.
Colors used should be green, white, yellow, blue. Clean pharmaceutical looking.
The Gumbra is easy to use, only one hand required and it is reusable.
On you tube I have 2 videos listed under "gumbra hd" Watch them for more info.
I am sending more variations of the "GUMBRA" logo that I have designed. They are very good variations.

Reason: Only have 5 responses. I thought there was to be at least 50.????

I am very sorry that I have not given any feed back. But there is a very good reason. I ALMOST DIED 4 TIMES.I was vomiting food on every meal and went through many tests to find the problem. It was determined that I had a diverticulum of the esophagus, or a bubble that if it had burst I would have died very quickly. I had a surgery on Feb 13, 2014 that was meant to fix this condition, But did not turn out very well for me. I have had 4 more surgeries since. I am doing much better now and I hope this last surgery will fix the problem. I again would like to apologize to all of the designers that submitted a design. Truly there was not much I could have done, I was fighting for my life. I would like to extend the date by an extra month from now if that is okay with all of the designers. You all have done a great job. And now that I have most of my energy back I can devote some time to completing this project. Most Respectfully Yours Dr. Martin L. Pelham

Target Market(s)

Anyone with teeth that gets food stuck in between them. Mostly adults , not really children, though I have my own kids who love them.

Industry/Entity Type

Dental

Requirements
Must have
• Clean, Healthy look and feel. A look that promotes health and well being.
• something pharmaceutical like. Clean colors blue,green, white, yellow.
Nice to have
• the advantages of Dr. designed, non-abrasive to tooth structure. Easy to use. Re-usable. Safe for dental implants.
Should not have
• old design, dark colors, i.e. browns, grays, nothing drab.

```html
<!DOCTYPE html>
<html lang="en">
<head>
<meta charset="utf-8">
<title>Gumbra 10 pcs carton dieline</title>
<link href="https://fonts.googleapis.com/css2?family=Open+Sans:wght@400;600;700;800&display=swap" rel="stylesheet">
<style>
:root{
  --stage:#f1f2f3;
  --deep:#1460ae;
  --mid:#1f82cc;
  --cyan:#2aa6e0;
  --light:#48bdee;
  --navy:#1d2a7a;
  --green:#5cc142;
  --yellow:#ffe14d;
  --white:#ffffff;
  --pale:#cdeefc;
  --ink:#0b3e78;
}
*{margin:0;padding:0;box-sizing:border-box}
html,body{width:1200px;height:1075px;overflow:hidden}
body{background:radial-gradient(ellipse at center,#ffffff 0%,var(--stage) 75%);font-family:"Open Sans",Arial,sans-serif;color:var(--white);position:relative}
.panel{position:absolute;overflow:hidden}
.back{left:310px;top:70px;width:570px;height:370px;background:linear-gradient(180deg,var(--mid) 0%,var(--deep) 100%)}
.back-inner{position:absolute;inset:0;transform:rotate(180deg)}
.slogan-band{position:absolute;left:0;right:0;background:linear-gradient(180deg,var(--cyan),var(--mid));display:flex;align-items:center;justify-content:center}
.top-face{left:310px;top:440px;width:570px;height:75px;background:linear-gradient(180deg,var(--cyan),var(--mid))}
.front{left:310px;top:515px;width:570px;height:355px;background:linear-gradient(180deg,var(--mid) 0%,var(--deep) 100%)}
.front-head{position:absolute;left:0;right:0;top:0;height:90px;background:linear-gradient(180deg,var(--light),var(--cyan));display:flex;align-items:center;justify-content:center}
.accent-rule{position:absolute;left:0;right:0;height:8px;background:linear-gradient(180deg,var(--green) 0 50%,var(--navy) 50%)}
.bottom-face{left:310px;top:870px;width:570px;height:95px;background:linear-gradient(180deg,var(--cyan),var(--light))}
.side-left{left:185px;top:540px;width:125px;height:340px;background:linear-gradient(180deg,var(--mid),var(--deep))}
.side-right{left:880px;top:500px;width:140px;height:350px;background:linear-gradient(180deg,var(--mid),var(--deep))}
.side-head{position:absolute;left:0;right:0;top:0;height:92px;background:linear-gradient(180deg,var(--light),var(--cyan))}
.headline{font-weight:600;letter-spacing:-.3px;white-space:nowrap}
.brand-row{position:absolute;display:flex;align-items:center;gap:6px}
.brand{font-weight:800;letter-spacing:1px;color:var(--white);line-height:1;white-space:nowrap}
.brand-dot{border-radius:50%;background:var(--green);flex:none}
.tagline{font-weight:700;white-space:nowrap}
.count{display:flex;align-items:center;font-weight:800;line-height:1}
.count .pcs{writing-mode:vertical-rl;transform:rotate(180deg);font-size:.42em;margin-left:2px}
.weight{font-weight:600;font-size:13px;white-space:nowrap}
.product-art{position:absolute;border-radius:60px 20px 60px 20px;background:radial-gradient(ellipse at 35% 50%,#ffffff 0%,#e3f5fd 35%,rgba(160,220,248,.55) 65%,rgba(160,220,248,0) 100%)}
.claim{font-weight:700;font-size:13px;letter-spacing:1.2px;text-align:center;line-height:1.45;color:var(--yellow);white-space:nowrap}
.fine{position:absolute;font-size:7px;line-height:1.35;color:var(--ink)}
.fine b{font-weight:700}
.seal{position:absolute;width:34px;height:34px;border:2px solid var(--white);border-radius:50%}
.seal-text{position:absolute;font-size:10px;font-weight:700;text-align:center;line-height:1.2}
.code-label{position:absolute;background:var(--white)}
.size-line{position:absolute;font-size:9px;font-weight:600;letter-spacing:.3px;color:var(--pale);white-space:nowrap}
</style>
</head>
<body>

<section class="panel back">
  <div class="back-inner">
    <div class="slogan-band" style="top:0;height:120px">
      <span class="headline" style="font-size:31px">Makes Every Smile Brightly Fresh!</span>
    </div>
    <div class="accent-rule" style="top:120px"></div>
    <div class="product-art" role="img" aria-label="Gumbra plaque remover pick illustration" style="left:20px;top:165px;width:260px;height:140px"></div>
    <div class="brand-row" style="left:300px;top:178px">
      <span class="brand" style="font-size:50px">GUMBRA</span><span class="brand-dot" style="width:12px;height:12px"></span>
    </div>
    <div class="tagline" style="position:absolute;left:304px;top:240px;font-size:14px">Makes Every Smile Brightly Fresh!</div>
    <div class="count" style="position:absolute;left:24px;top:315px;font-size:38px">10<span class="pcs">PCS</span></div>
    <div class="weight" style="position:absolute;left:110px;top:332px">50 gr. (17.6 oz)</div>
  </div>
</section>

<section class="panel top-face">
  <div class="brand-row" style="left:22px;top:12px">
    <span class="brand" style="font-size:24px">GUMBRA</span><span class="brand-dot" style="width:7px;height:7px"></span>
  </div>
  <div class="tagline" style="position:absolute;left:24px;top:44px;font-size:9px">Makes Every Smile Brightly Fresh!</div>
  <div class="count" style="position:absolute;left:345px;top:8px;font-size:34px">10<span class="pcs">PCS</span></div>
  <div class="weight" style="position:absolute;left:430px;top:22px;font-size:11px">50 gr. (17.6 oz)</div>
  <div class="size-line" style="left:250px;top:56px">SIZE: 2FT x 2FT 4IN x 4MIL (60.0 CM x 71.1 CM x 10.1 µm)</div>
</section>

<section class="panel front">
  <div class="front-head"><span class="headline" style="font-size:29px">Makes Every Smile Brightly Fresh!</span></div>
  <div class="accent-rule" style="top:90px"></div>
  <div class="product-art" role="img" aria-label="Gumbra plaque remover pick illustration" style="left:20px;top:115px;width:260px;height:130px"></div>
  <div class="brand-row" style="left:298px;top:128px">
    <span class="brand" style="font-size:50px">GUMBRA</span><span class="brand-dot" style="width:12px;height:12px"></span>
  </div>
  <div class="tagline" style="position:absolute;left:300px;top:190px;font-size:14px">Makes Every Smile Brightly Fresh!</div>
  <div class="count" style="position:absolute;left:22px;top:258px;font-size:46px">10<span class="pcs">PCS</span></div>
  <div class="weight" style="position:absolute;left:24px;top:318px">50 gr. (17.6 oz)</div>
  <div class="claim" style="position:absolute;left:285px;top:268px;width:270px">ANATOMICALLY AND ERGONOMICALLY<br>CORRECT DENTAL PLAQUE REMOVER</div>
</section>

<section class="panel bottom-face">
  <div class="seal" style="left:30px;top:8px"></div>
  <div class="seal-text" style="left:8px;top:46px;width:80px">100%<br>Recycled<br>Paperboard</div>
  <p class="fine" style="left:100px;top:10px;width:200px"><b>WARNING:</b> To avoid danger of choking, keep this pack away from babies and children. Do not use in cribs. <b>Advertencia:</b> mantener lejos de los niños. Store in a dry place. Recycle when empty. Made for Pelham Dental Co., P.O. Box 210, Fairview, USA.</p>
  <p class="fine" style="left:315px;top:10px;width:200px"><b>WARNING:</b> To avoid danger of choking, keep this pack away from babies and children. Do not use in cribs. <b>Advertencia:</b> mantener lejos de los niños. Store in a dry place. Recycle when empty. Made for Pelham Dental Co., P.O. Box 210, Fairview, USA.</p>
  <div class="code-label" style="left:528px;top:8px;width:30px;height:78px"></div>
</section>

<section class="panel side-left">
  <div class="side-head"></div>
  <div class="accent-rule" style="top:92px"></div>
  <div class="brand-row" style="left:12px;top:28px">
    <span class="brand" style="font-size:20px">GUMBRA</span><span class="brand-dot" style="width:6px;height:6px"></span>
  </div>
  <div class="tagline" style="position:absolute;left:12px;top:54px;font-size:6.5px">Makes Every Smile Brightly Fresh!</div>
  <div class="count" style="position:absolute;left:14px;top:220px;font-size:44px">10<span class="pcs">PCS</span></div>
  <div class="weight" style="position:absolute;left:16px;top:280px">50 gr. (17.6 oz)</div>
</section>

<section class="panel side-right">
  <div class="side-head" style="height:98px"></div>
  <div class="accent-rule" style="top:98px"></div>
  <div class="brand-row" style="left:16px;top:30px">
    <span class="brand" style="font-size:21px">GUMBRA</span><span class="brand-dot" style="width:6px;height:6px"></span>
  </div>
  <div class="tagline" style="position:absolute;left:16px;top:57px;font-size:7px">Makes Every Smile Brightly Fresh!</div>
  <div class="count" style="position:absolute;left:18px;top:210px;font-size:46px">10<span class="pcs">PCS</span></div>
  <div class="weight" style="position:absolute;left:20px;top:272px">50 gr. (17.6 oz)</div>
</section>

</body>
</html>
```